Business Card Design for Funky New Cloud Security Start-up

We're looking for kick ass business cards to make use stand out from the crowd in a world that's dominated by dull, boring, blue logos.

We have a logo (designed here on make forge) and we'd like to build on the brand theme of "Security made simple."

Please use following details for sample:

Peter Holmsby
CEO
+61 (0)4127 568 213
pete@varqel.com

2708/46 Tamberly Street
Sydney NSW 2000
Australia

Target Market(s)

Customers will be large enterprise clients - typically VP level. Also resellers of our product who are mid-tier.

Industry/Entity Type

Business

Font styles to use
Sans Serif

Requirements
Must have
• Use the colour scheme from the attached logo
Do not put space for a fax - it's old school
Easy to use on quill press
Use a font that complements the logo font

```html
<!DOCTYPE html>
<html lang="en">
<head>
<meta charset="utf-8">
<title>varqel business cards</title>
<link rel="stylesheet" href="https://fonts.googleapis.com/css2?family=Comfortaa:wght@400;500;700&display=swap">
<style>
  :root {
    --backdrop: #1c1c1c;
    --card-white: #ffffff;
    --brand-grey: #5f5f5f;
    --brand-blue: #2a8fc4;
    --deep-teal: #1f5673;
    --mid-blue: #2a7aa3;
    --lime: #a9cf3c;
    --ink-dark: #1d3a45;
    --white: #ffffff;
  }
  * { margin: 0; padding: 0; box-sizing: border-box; }
  html, body {
    width: 1200px; height: 1200px; overflow: hidden;
    background: var(--backdrop);
    font-family: "Comfortaa", sans-serif;
  }
  .canvas { position: relative; width: 1200px; height: 1200px; }

  .card { position: absolute; width: 740px; height: 420px; }

  .card-front {
    left: 60px; top: 110px;
    background: var(--card-white);
    display: flex; align-items: center; justify-content: center;
  }
  .front-mark { display: flex; align-items: center; gap: 22px; }
  .front-mark .dot {
    width: 90px; height: 90px; border-radius: 50%;
    background: var(--brand-blue);
  }
  .front-mark .wordmark {
    font-size: 118px; font-weight: 500; color: var(--brand-grey);
    letter-spacing: -2px; line-height: 1;
  }

  .card-back {
    left: 400px; top: 650px;
    background: radial-gradient(ellipse at 60% 50%, var(--mid-blue) 0%, var(--deep-teal) 85%);
    color: var(--white);
  }
  .back-mark {
    position: absolute; left: 70px; top: 48px;
    display: flex; align-items: center; gap: 16px;
  }
  .back-mark .dot { width: 62px; height: 62px; border-radius: 50%; background: var(--white); }
  .back-mark .wordmark { font-size: 86px; font-weight: 500; color: var(--white); line-height: 1; letter-spacing: -1px; }

  .name-row { position: absolute; left: 0; top: 176px; display: flex; align-items: center; }
  .name-band {
    background: var(--lime); color: var(--ink-dark);
    font-size: 30px; font-weight: 500; text-transform: uppercase; letter-spacing: 1px;
    padding: 10px 20px 8px 100px;
  }
  .role { color: var(--lime); font-size: 30px; font-weight: 500; margin-left: 8px; }

  .address {
    position: absolute; left: 40px; top: 306px;
    display: flex; gap: 14px; color: var(--lime);
    font-size: 23px; line-height: 1.35;
  }
  .address svg { width: 26px; height: 26px; flex: none; margin-top: 2px; }

  .contact {
    position: absolute; right: 24px; bottom: 30px;
    transform-origin: right bottom;
    transform: rotate(-90deg) translateX(100%);
    font-size: 23px; line-height: 1.4; white-space: nowrap;
  }
  .contact-line { display: flex; align-items: center; gap: 10px; }
  .contact-line svg { width: 20px; height: 20px; transform: rotate(90deg); }
</style>
</head>
<body>
<main class="canvas">
  <section class="card card-front" aria-label="Card front">
    <div class="front-mark">
      <span class="dot"></span>
      <span class="wordmark">varqel.</span>
    </div>
  </section>

  <section class="card card-back" aria-label="Card back">
    <div class="back-mark">
      <span class="dot"></span>
      <span class="wordmark">varqel.</span>
    </div>

    <div class="name-row">
      <span class="name-band">Peter Holmsby</span>
      <span class="role">CEO</span>
    </div>

    <div class="address">
      <svg viewBox="0 0 24 24" aria-hidden="true"><path fill="#ffffff" d="M12 2 1 12h3v10h6v-6h4v6h6V12h3z"/></svg>
      <p>2708/46 Tamberly Street<br>Sydney NSW 2000 Australia</p>
    </div>

    <div class="contact">
      <p class="contact-line">
        <svg viewBox="0 0 24 24" aria-hidden="true"><path fill="#ffffff" d="M6.6 10.8a15.1 15.1 0 0 0 6.6 6.6l2.2-2.2a1 1 0 0 1 1-.25 11.4 11.4 0 0 0 3.6.57 1 1 0 0 1 1 1V20a1 1 0 0 1-1 1A17 17 0 0 1 3 4a1 1 0 0 1 1-1h3.5a1 1 0 0 1 1 1c0 1.25.2 2.45.57 3.57a1 1 0 0 1-.25 1z"/></svg>
        +61 (0)4127 568 213
      </p>
      <p class="contact-line">
        <svg viewBox="0 0 24 24" aria-hidden="true"><path fill="#ffffff" d="M2 5h20v14H2zm2 2v.4l8 5 8-5V7z"/></svg>
        pete@varqel.com
      </p>
    </div>
  </section>
</main>
</body>
</html>
```